Global Weight loss program

we need a business card based in Brooklyn , NY called ZestwellPRO . Mara Tullin Opdegard the founder and creator of ZestwellPRO Movement. A business based around nutrition, health, Whole Foods and fitness.

Industry/Entity Type

Food Service

Contact Information for Business Card

Phone number : 718-402-3859
website www.zestwellpro.example
email : mara@zestwellpro.example

Font styles to use
Sans Serif

Requirements
Must have
• logo colors
• green black and gold
Nice to have
• must be simple and sharp.
Should not have
• pictures of items

```html
<!DOCTYPE html>
<html lang="en">
<head>
<meta charset="utf-8">
<title>ZestwellPRO Business Card</title>
<link href="https://fonts.googleapis.com/css2?family=Open+Sans:wght@400;600;700&display=swap" rel="stylesheet">
<style>
  :root {
    --backdrop: #4b423b;
    --card: #0d0d0d;
    --card-edge: #1c1c1c;
    --ink-light: #e9e9e9;
    --ink-muted: #bdbdbd;
    --silver: #c9c9c9;
    --green: #8cd11e;
    --divider: #262626;
  }
  * { margin: 0; padding: 0; box-sizing: border-box; }
  html, body {
    width: 1200px; height: 900px; overflow: hidden;
    background: var(--backdrop);
    font-family: "Open Sans", Arial, sans-serif;
  }
  .stage {
    position: relative; width: 1200px; height: 900px;
    display: flex; align-items: center; justify-content: center; gap: 40px;
  }
  .card {
    position: relative; width: 540px; height: 309px;
    background: var(--card);
    border: 1px solid var(--card-edge);
    box-shadow: 0 14px 30px rgba(0,0,0,.45);
  }
  /* front */
  .card-front { display: flex; }
  .front-brand {
    width: 50%; display: flex; align-items: center; justify-content: center; gap: 10px;
  }
  .brand-dot {
    width: 14px; height: 14px; border-radius: 50%; background: var(--green);
  }
  .brand-name {
    font-weight: 700; font-size: 28px; color: var(--ink-light); letter-spacing: .2px;
  }
  .front-divider {
    width: 1px; background: var(--divider); margin: 0;
  }
  .front-info {
    flex: 1; padding: 72px 0 0 30px; color: var(--ink-light);
  }
  .person-name { font-weight: 700; font-size: 18px; line-height: 1.2; color: var(--silver); }
  .person-name .surname { color: var(--green); }
  .person-role { font-size: 13px; color: var(--ink-muted); margin-top: 2px; }
  .contact-list { list-style: none; margin-top: 22px; }
  .contact-list li {
    display: flex; align-items: center; gap: 10px;
    font-size: 13.5px; color: var(--ink-light); margin-bottom: 6px;
  }
  .contact-list svg { width: 11px; height: 11px; fill: var(--green); flex: none; }
  /* back */
  .card-back {
    display: flex; flex-direction: column; align-items: center; justify-content: center;
  }
  .back-mark {
    width: 56px; height: 56px; border-radius: 50%;
    background: linear-gradient(160deg, #e4e4e4, #8e8e8e);
    margin-bottom: 22px;
  }
  .back-name {
    font-weight: 700; font-size: 40px; color: var(--silver); line-height: 1;
  }
  .back-tagline {
    margin-top: 6px; font-size: 11px; letter-spacing: 1.6px; color: var(--ink-muted);
  }
</style>
</head>
<body>
<main class="stage">
  <section class="card card-front">
    <div class="front-brand">
      <span class="brand-dot"></span>
      <span class="brand-name">ZestwellPRO</span>
    </div>
    <div class="front-divider"></div>
    <div class="front-info">
      <p class="person-name">Mara Tullin <span class="surname">Opdegard</span></p>
      <p class="person-role">Founder</p>
      <ul class="contact-list">
        <li>
          <svg viewBox="0 0 24 24"><path d="M6.6 10.8a15.1 15.1 0 0 0 6.6 6.6l2.2-2.2a1 1 0 0 1 1-.25 11.4 11.4 0 0 0 3.6.57 1 1 0 0 1 1 1V20a1 1 0 0 1-1 1A17 17 0 0 1 3 4a1 1 0 0 1 1-1h3.5a1 1 0 0 1 1 1c0 1.25.2 2.45.57 3.57a1 1 0 0 1-.25 1z"/></svg>
          718-402-3859
        </li>
        <li>
          <svg viewBox="0 0 24 24"><path d="M2 5h20v14H2z M2 5l10 8 10-8" /></svg>
          mara@zestwellpro.example
        </li>
        <li>
          <svg viewBox="0 0 24 24"><circle cx="12" cy="12" r="10"/></svg>
          www.zestwellpro.example
        </li>
      </ul>
    </div>
  </section>

  <section class="card card-back">
    <span class="back-mark"></span>
    <p class="back-name">ZestwellPRO</p>
    <p class="back-tagline">Fitness, Nutrition and Health</p>
  </section>
</main>
</body>
</html>
```